Valkemo App for Smart Devices IoT WiFi Electronic

Valkemo is a siren manufacturer. This application is used for the company's products that have a Wi-Fi connection and an internet connection, which can be configured and activated remotely through this application. In addition, this application is used to activate the siren at specific times for the start and end of shifts in companies and schools. Users will be siren installers and IT or HR managers.
In addition to activating motorized sirens timers, some siren models have speakers and allow you to play TTS (text to speech) audio, audio recorded by the user on the phone and upload audio (mp3) with playlist programming with start and end times.
Application screens: home with dashboard (one dashboard for each category). Device categories: timers, speakers, motorized siren. Screen for requesting evaluation in the Play Store. Screen for registering the user profile. Screen for registering devices according to their category (timers, speakers, motorized siren). Screen for registering device groups. Screen for pairing the device on the client's Wi-Fi network. Screen for registering activation times. Screen for uploading MP3 audios. Screen for registering playlists with audio selection, start and end times. Screen for recording audio for later sending to the speakers. Screen for converting text to speech and sending to the speakers. It is important to have a time picker with the day of the week to program the activation times and playlist.

Target Market(s)

Schools, Companies and Stores.

Industry/Entity Type

IoT

Font styles to use
Sans Serif
Other font styles liked:
• roboto

Colors
FFC000
F8CF3A
FAE287
FDF2CF
FEFAEE

Requirements
Must have
• time picker with weekdays for timer programming feature.
Nice to have
• app review request screen on play store

```html
<!DOCTYPE html>
<html lang="en">
<head>
<meta charset="utf-8">
<title>Valkemo – Timer</title>
<link href="https://fonts.googleapis.com/css2?family=Poppins:wght@400;500;600;700;800&display=swap" rel="stylesheet">
<style>
:root{
  --yellow:#f7bd00;
  --ink:#4a5263;
  --muted:#3f4654;
  --line:#e3e6ec;
  --chip:#eceef1;
  --bg:#f5f6f9;
  --page:#eef0f4;
  --white:#ffffff;
  --icon:#a9b0bb;
  --online:#3cc94a;
}
*{margin:0;padding:0;box-sizing:border-box}
html,body{width:677px;height:1200px;overflow:hidden;background:var(--page);font-family:"Poppins",sans-serif}
.screen{position:absolute;left:110px;top:85px;width:485px;height:1045px;background:var(--bg);border-radius:44px;overflow:hidden}
.header-shape{position:absolute;left:0;top:0}
.status{position:absolute;top:18px;left:38px;right:26px;display:flex;justify-content:space-between;align-items:center;color:var(--muted);font-weight:600;font-size:17px}
.title{position:absolute;top:72px;left:0;width:100%;text-align:center;color:var(--white);font-weight:700;font-size:32px;line-height:50px}
.back{position:absolute;left:22px;top:87px}
.avatar{position:absolute;left:398px;top:66px;width:60px;height:60px;border-radius:50%;border:3px solid var(--white);background:linear-gradient(135deg,#c9b39a,#8a7a6c)}
.online{position:absolute;left:448px;top:70px;width:12px;height:12px;border-radius:50%;background:var(--online);border:2px solid var(--white)}
.card{position:absolute;left:25px;width:433px;background:var(--white);border-radius:16px;box-shadow:0 8px 24px rgba(60,70,90,.08)}
.card-settings{top:177px;height:404px}
.card-repeat{top:601px;height:233px}
.label{position:absolute;left:37px;color:var(--ink);font-weight:700;font-size:18px}
.field{position:absolute;left:35px;width:359px;height:58px;border:1px solid var(--line);border-radius:29px;display:flex;align-items:center;justify-content:space-between;padding:0 22px 0 26px;font-size:13px;color:var(--muted)}
.options{position:absolute;left:38px;top:70px;display:flex;gap:19px;font-size:11.5px;font-weight:500;color:var(--ink)}
.option{display:flex;align-items:center;gap:4px}
.radio{width:12px;height:12px;border-radius:50%;border:1.6px solid var(--ink)}
.option.active{color:var(--yellow)}
.option.active .radio{border-color:var(--yellow);background:radial-gradient(circle,var(--yellow) 0 3px,transparent 3.5px)}
.divider{position:absolute;left:35px;top:105px;width:364px;height:1px;background:var(--line)}
.days{position:absolute;left:34px;top:130px;width:320px;display:flex;flex-wrap:wrap;gap:12px 10px}
.day{width:68px;height:30px;border-radius:15px;background:var(--chip);color:var(--ink);font-size:11.5px;font-weight:600;display:flex;align-items:center;justify-content:center;gap:4px}
.day.on{background:var(--yellow);color:var(--white)}
.save{position:absolute;left:327px;top:861px;width:131px;height:51px;border-radius:26px;background:var(--yellow);color:var(--white);font-weight:800;font-size:17px;letter-spacing:.5px;display:flex;align-items:center;justify-content:center}
.nav{position:absolute;left:0;top:943px;width:100%;height:102px;background:var(--white)}
.nav svg{position:absolute;top:22px}
.home-bar{position:absolute;left:151px;top:76px;width:175px;height:6px;border-radius:3px;background:#b0b7c3}
</style>
</head>
<body>
<main class="screen">
  <svg class="header-shape" width="485" height="200" viewBox="0 0 485 200" aria-hidden="true">
    <path d="M0 0H485V120C485 150 475 175 462 195C440 180 420 177 400 177H85C65 177 45 180 25 195C10 175 0 150 0 120Z" fill="var(--yellow)"/>
  </svg>
  <div class="status">
    <span>9:41</span>
    <svg width="74" height="14" viewBox="0 0 74 14" aria-hidden="true" fill="var(--muted)">
      <rect x="0" y="9" width="3" height="5" rx="1"/><rect x="5" y="6" width="3" height="8" rx="1"/><rect x="10" y="3" width="3" height="11" rx="1"/><rect x="15" y="0" width="3" height="14" rx="1"/>
      <path d="M25 5a11 11 0 0 1 15 0l-2 2a8 8 0 0 0-11 0zM28 8a6 6 0 0 1 9 0l-2 2a3 3 0 0 0-5 0zM32.5 11l2 2-2 1.5-2-1.5z"/>
      <rect x="47" y="1" width="24" height="12" rx="3" fill="none" stroke="var(--muted)" stroke-width="1.2"/><rect x="49" y="3" width="20" height="8" rx="1.5"/><rect x="72" y="5" width="2" height="4" rx="1"/>
    </svg>
  </div>
  <svg class="back" width="16" height="22" viewBox="0 0 16 22" aria-hidden="true"><path d="M12 3L4 11l8 8" fill="none" stroke="var(--white)" stroke-width="3" stroke-linecap="round" stroke-linejoin="round"/></svg>
  <h1 class="title">Timer</h1>
  <div class="avatar" role="img" aria-label="User profile photo"></div>
  <span class="online"></span>

  <section class="card card-settings">
    <h2 class="label" style="top:30px">Select Device</h2>
    <div class="field" style="top:65px"><span>Select</span>
      <svg width="14" height="8" viewBox="0 0 14 8" aria-hidden="true"><path d="M1 1l6 6 6-6" fill="none" stroke="#8a909b" stroke-width="1.6" stroke-linecap="round"/></svg></div>
    <h2 class="label" style="top:150px">Select Audio From Media</h2>
    <div class="field" style="top:185px"><span>Choose MP3 Audio</span>
      <svg width="18" height="18" viewBox="0 0 18 18" aria-hidden="true" fill="none" stroke="#7d838e" stroke-width="1.5" stroke-linecap="round" stroke-linejoin="round"><path d="M9 12V2M5 6l4-4 4 4M2 11v4a1 1 0 0 0 1 1h12a1 1 0 0 0 1-1v-4"/></svg></div>
    <h2 class="label" style="top:271px">Duration</h2>
    <div class="field" style="top:306px"><span>Select Time</span>
      <svg width="19" height="19" viewBox="0 0 19 19" aria-hidden="true" fill="none" stroke="#8a909b" stroke-width="1.5" stroke-linecap="round"><circle cx="9.5" cy="9.5" r="8.3"/><path d="M9.5 5v5l3 2"/></svg></div>
  </section>

  <section class="card card-repeat">
    <h2 class="label" style="top:25px">Repeat Activation</h2>
    <div class="options">
      <span class="option"><i class="radio"></i>Only Once</span>
      <span class="option"><i class="radio"></i>Daily</span>
      <span class="option"><i class="radio"></i>Weekly</span>
      <span class="option active"><i class="radio"></i>Custom Input</span>
    </div>
    <div class="divider"></div>
    <div class="days">
      <span class="day on"><svg width="10" height="10" viewBox="0 0 10 10" aria-hidden="true"><circle cx="5" cy="5" r="5" fill="#fff"/><path d="M2.8 5.1l1.5 1.5 3-3" fill="none" stroke="var(--yellow)" stroke-width="1.4"/></svg>MON</span>
      <span class="day on"><svg width="10" height="10" viewBox="0 0 10 10" aria-hidden="true"><circle cx="5" cy="5" r="5" fill="#fff"/><path d="M2.8 5.1l1.5 1.5 3-3" fill="none" stroke="var(--yellow)" stroke-width="1.4"/></svg>TUE</span>
      <span class="day">WED</span>
      <span class="day on"><svg width="10" height="10" viewBox="0 0 10 10" aria-hidden="true"><circle cx="5" cy="5" r="5" fill="#fff"/><path d="M2.8 5.1l1.5 1.5 3-3" fill="none" stroke="var(--yellow)" stroke-width="1.4"/></svg>THU</span>
      <span class="day">FRI</span>
      <span class="day">SAT</span>
      <span class="day">SUN</span>
    </div>
  </section>

  <div class="save">SAVE</div>

  <nav class="nav">
    <svg style="left:62px" width="28" height="28" viewBox="0 0 28 28" aria-hidden="true"><path d="M14 2L2 12v13a2 2 0 0 0 2 2h6v-8h8v8h6a2 2 0 0 0 2-2V12z" fill="var(--yellow)"/></svg>
    <svg style="left:170px" width="32" height="32" viewBox="0 0 32 32" aria-hidden="true"><circle cx="16" cy="16" r="16" fill="var(--icon)"/><path d="M16 9v14M9 16h14" stroke="#fff" stroke-width="3" stroke-linecap="round"/></svg>
    <svg style="left:284px" width="26" height="32" viewBox="0 0 26 32" aria-hidden="true" fill="var(--icon)"><path d="M13 1a2 2 0 0 1 2 2v1.5A9 9 0 0 1 22 13v7l3 4H1l3-4v-7a9 9 0 0 1 7-8.5V3a2 2 0 0 1 2-2z"/><path d="M9 27h8a4 4 0 0 1-8 0z"/></svg>
    <svg style="left:391px" width="32" height="32" viewBox="0 0 32 32" aria-hidden="true"><path fill="var(--icon)" d="M13.5 1h5l.8 4.2 3 1.3 3.6-2.4 3.5 3.5-2.4 3.6 1.3 3 4.2.8v5l-4.2.8-1.3 3 2.4 3.6-3.5 3.5-3.6-2.4-3 1.3-.8 4.2h-5l-.8-4.2-3-1.3-3.6 2.4-3.5-3.5 2.4-3.6-1.3-3L0 18.5v-5l4.2-.8 1.3-3-2.4-3.6 3.5-3.5 3.6 2.4 3-1.3z"/><circle cx="16" cy="16" r="5" fill="#fff"/></svg>
    <span class="home-bar"></span>
  </nav>
</main>
</body>
</html>
```